What makes us Different Managed Communications Services Provider Flyer

We need a flyer to explain why we are different than other "managed IT services" company. Gives a brief description of our company and services that can entice clients and potential clients to setup a FREE consultation with us. This will become part of an ongoing marketing campaign that includes emails, leave behinds, brochures, and more

```html
<!DOCTYPE html>
<html lang="en">
<head>
<meta charset="utf-8">
<title>Summit Line Networks – What Makes Us Different</title>
<link href="https://fonts.googleapis.com/css2?family=Roboto:ital,wght@0,400;0,500;0,700;0,900;1,400;1,700;1,900&display=swap" rel="stylesheet">
<style>
  :root{
    --navy:#1c2340;
    --ink:#1a1f3a;
    --blue:#2f5fb3;
    --sky-top:#a8bcdf;
    --sky-bottom:#bfd0ec;
    --gold:#f2c21b;
    --white:#ffffff;
    --black-box:#0b0d18;
  }
  *{box-sizing:border-box;margin:0;padding:0}
  html,body{width:846px;height:1200px;overflow:hidden;background:var(--white)}
  body{font-family:"Roboto",Arial,sans-serif;color:var(--ink)}
  .flyer{position:relative;width:846px;height:1200px;overflow:hidden;background:var(--white)}

  /* left column */
  .brand{position:absolute;left:40px;top:36px;display:flex;align-items:center;gap:14px}
  .brand-square{width:46px;height:46px;background:var(--navy)}
  .brand-name{font-size:30px;font-weight:900;color:var(--navy);letter-spacing:.3px;line-height:1}

  .city-art{position:absolute;left:0;top:130px;width:410px;height:630px;
    background:linear-gradient(180deg,#f3f5fa 0%,#c9d2e6 22%,#4a5a8c 50%,#2a3563 75%,var(--navy) 100%)}

  .legacy{position:absolute;left:0;top:760px;width:410px;height:440px;background:var(--navy);color:var(--white);padding:20px 22px 0}
  .legacy-title{text-align:center;font-size:18px;font-weight:700;line-height:28px}
  .legacy-title .accent{color:var(--gold);display:block}
  .legacy-text{margin-top:14px;text-align:center;font-size:11px;line-height:14.5px}
  .contact-title{margin-top:22px;margin-left:4px;color:var(--gold);font-size:20px;font-weight:900;font-style:italic;line-height:24px}
  .contact-list{margin-top:8px;margin-left:4px;list-style:none;font-size:12px;line-height:20.5px}
  .contact-list li{display:flex;align-items:center;gap:10px}
  .contact-list svg{width:11px;height:11px;fill:var(--gold)}
  .badge-square{position:absolute;left:344px;top:332px;width:62px;height:60px;background:var(--black-box)}

  /* right column */
  .details{position:absolute;left:410px;top:0;width:436px;height:1200px;
    background:linear-gradient(180deg,var(--sky-top) 0%,var(--sky-bottom) 100%);padding:56px 16px 0 18px}
  .section-title{font-size:21px;font-weight:700;color:var(--ink);line-height:26px}
  .body-text{font-size:12px;line-height:16px;margin-top:6px}
  .body-text + .body-text{margin-top:0}
  .lead{font-style:italic;color:var(--blue);font-size:12.5px;margin-top:4px}
  .sub{font-style:italic;font-size:12.5px;margin-top:10px}
  .gap{margin-top:18px}

  .services{position:relative;height:220px;margin-top:12px}
  .service{position:absolute;display:flex;align-items:center;gap:8px;font-size:12px;line-height:15px}
  .service strong{color:var(--blue);font-weight:700;display:block}
  .service .icon{width:20px;height:20px;flex:none;fill:none;stroke:var(--blue);stroke-width:2}
  .service.s1{left:14px;top:0}
  .service.s2{right:8px;top:50px;text-align:right}
  .service.s3{left:14px;top:104px}
  .service.s4{right:8px;top:156px;text-align:right}

  .site{position:absolute;left:0;right:0;top:1146px;text-align:center;font-size:12px}
</style>
</head>
<body>
<div class="flyer">

  <div class="brand">
    <span class="brand-square"></span>
    <span class="brand-name">Summit Line<br>Networks</span>
  </div>

  <div class="city-art" role="img" aria-label="Illustration of a dark blue isometric city skyline with lit office towers"></div>

  <section class="legacy">
    <h2 class="legacy-title">More Than Just a Managed IT Provider –<span class="accent">Our Legacy of Excellence</span></h2>
    <p class="legacy-text">At our company we are far more than your typical managed IT provider. Since our founding in 1983, we have built a reputation based on trust, reliability, and unparalleled service. With client relationships spanning 20 to 30 years, we have demonstrated a level of commitment that few IT firms can match. What sets us apart is not just our technical expertise but the deep, long-term partnerships we cultivate with our clients—many of whom have stayed with us without ever being locked into a contract. That is a testament to the exceptional quality of our service and the trust we have earned over decades.</p>
    <h3 class="contact-title">Contact Us</h3>
    <ul class="contact-list">
      <li><svg viewBox="0 0 12 12"><path d="M6 0a4 4 0 0 0-4 4c0 3 4 8 4 8s4-5 4-8a4 4 0 0 0-4-4zm0 5.5A1.5 1.5 0 1 1 6 2.5a1.5 1.5 0 0 1 0 3z"/></svg>Riverton, Ohio</li>
      <li><svg viewBox="0 0 12 12"><path d="M2.5 0 4.5 2.5 3.3 4a7 7 0 0 0 4.7 4.7L9.5 7.5 12 9.5 10.5 12C5 12 0 7 0 1.5z"/></svg>(555) 014-2290</li>
      <li><svg viewBox="0 0 12 12"><path d="M0 2h12v8H0zm1 1 5 4 5-4z"/></svg>Lorem Lorem</li>
      <li><svg viewBox="0 0 12 12"><circle cx="6" cy="6" r="6"/></svg>summitlinenet.com</li>
    </ul>
    <div class="badge-square"></div>
  </section>

  <section class="details">
    <h2 class="section-title">A Commitment Beyond Contracts</h2>
    <p class="body-text">Unlike many managed IT providers who rely on rigid contracts to retain clients, we believe that service excellence speaks for itself. The longevity of our client relationships is rooted in our ability to anticipate needs, resolve challenges before they escalate, and proactively enhance network &amp; communication infrastructures. Our comprehensive checklists, questionnaires, policies, and procedures, attention to details ensure that every client receives a tailored, best-in-class experience from day one.</p>

    <h2 class="section-title gap">A Holistic Approach to IT Management</h2>
    <p class="body-text">We don't just manage IT—we integrate ourselves into your business, ensuring that technology aligns with your strategic goals. Our services go beyond traditional break-fix support.</p>
    <p class="lead">We offer:</p>

    <div class="services">
      <div class="service s1">
        <svg class="icon" viewBox="0 0 20 20"><circle cx="10" cy="10" r="8"/><circle cx="10" cy="10" r="3"/></svg>
        <span><strong>Strategic IT Roadmaps</strong>customized to drive business growth</span>
      </div>
      <div class="service s2">
        <span><strong>Proactive cybersecurity assessments</strong>help keep businesses secure</span>
        <svg class="icon" viewBox="0 0 20 20"><path d="M10 2 17 5v5c0 4-3 7-7 8-4-1-7-4-7-8V5z"/></svg>
      </div>
      <div class="service s3">
        <svg class="icon" viewBox="0 0 20 20"><path d="M6 15h9a3.5 3.5 0 0 0 0-7 5 5 0 0 0-9.5 1A3 3 0 0 0 6 15z"/></svg>
        <span><strong>Comprehensive backup &amp;<br>disaster recovery solutions</strong>provide peace of mind</span>
      </div>
      <div class="service s4">
        <span><strong>Industry-leading response times &amp;<br>dedicated support teams</strong>focused on delivering<br>an exceptional client experience</span>
        <svg class="icon" viewBox="0 0 20 20"><path d="M3 12V10a7 7 0 0 1 14 0v2M3 12h3v4H3zm11 0h3v4h-3z"/></svg>
      </div>
    </div>

    <h2 class="section-title">Our Clients Stay Because We Deliver</h2>
    <p class="sub">Over 40 years</p>
    <p class="body-text">We have maintained a standard of excellence that other companies simply cannot compare with. Our team of experts consistently goes above and beyond, ensuring that clients not only get the support they need but also receive the strategic guidance necessary to stay ahead in an ever-evolving digital landscape.</p>
    <p class="sub">90-day performance review process</p>
    <p class="body-text">Ensures we continuously improve our services based on client feedback. This process allows us to adapt, refine, and enhance our approach, providing a truly personalized IT experience that aligns with business objectives.</p>

    <h2 class="section-title gap">A Legacy of Trust &amp; Reliability</h2>
    <p class="body-text">The fact that many of our clients have remained with us for decades without a formal contract speaks volumes about the trust we have built. We don't lock in clients with paperwork—we keep them with results. That's the difference between a standard managed IT provider and an IT partner who genuinely cares.</p>
    <p class="body-text">If you're looking for an IT provider that will treat your business as if it were their own, look no further. Our legacy of service, innovation, and commitment to our clients is what sets us apart from the rest.</p>

    <p class="site">summitlinenet.com</p>
  </section>

</div>
</body>
</html>
```